Design for a 4 screens mobile app: Brelluvo

The app is a compact but illustrated phone/address book...
We need a design for the 5 screens of the app (see screens attached):
a) "index" : 1 screen with 6 pictures of contact person
b) "contact list" : 1 screen, to manage (add/del/edit) the contacts of the phone/address book
c) "add contact" : 1 screen to add a contact (a picture + a phone number)
d) "update contact" : similar to "add"
e) "fields missing" : add/edit screens in "error" state
We also need the ico design + loading screen.
No specific guidelines, nor logo or whatever.
It will be a free app distributed on iOS and Androïd.
We just want to make it looking nice & very usable for end users.
B2C

```html
<!DOCTYPE html>
<html lang="en">
<head>
<meta charset="utf-8">
<title>Brelluvo – Add Contact</title>
<link href="https://fonts.googleapis.com/css2?family=Mulish:wght@400;500;600;700&display=swap" rel="stylesheet">
<style>
  :root {
    --bar: #86a0b7;
    --bar-light: #93acc2;
    --bar-ink: #ffffff;
    --page: #ffffff;
    --field-border: #e2e6ea;
    --field-ink: #b7c6d2;
    --photo-dark: #1f3a22;
    --photo-mid: #3f6a3a;
    --photo-light: #a9b9a0;
    --photo-shirt: #a9c1de;
  }
  * { box-sizing: border-box; margin: 0; padding: 0; }
  html, body {
    width: 777px; height: 1200px; overflow: hidden;
    background: var(--page);
    font-family: "Mulish", "Helvetica Neue", Arial, sans-serif;
  }
  .screen { position: relative; width: 777px; height: 1200px; background: var(--page); }

  .top-bar {
    position: absolute; left: 0; top: 0; width: 777px; height: 162px;
    background: linear-gradient(105deg, var(--bar) 0%, var(--bar-light) 100%);
    color: var(--bar-ink);
  }
  .status-bar {
    position: absolute; left: 0; top: 0; width: 100%; height: 56px;
    display: flex; align-items: center; justify-content: space-between;
    padding: 0 24px; font-size: 22px; font-weight: 500;
  }
  .status-left, .status-right { display: flex; align-items: center; gap: 8px; width: 220px; }
  .status-right { justify-content: flex-end; }
  .signal { display: flex; gap: 3px; }
  .signal span { width: 12px; height: 12px; border-radius: 50%; border: 1.5px solid var(--bar-ink); }
  .signal span.on { background: var(--bar-ink); }
  .battery { width: 48px; height: 18px; border: 2px solid var(--bar-ink); border-radius: 3px; padding: 2px; position: relative; }
  .battery::after { content: ""; position: absolute; right: -5px; top: 4px; width: 3px; height: 6px; background: var(--bar-ink); }
  .battery-fill { width: 100%; height: 100%; background: var(--bar-ink); }

  .nav-bar {
    position: absolute; left: 0; top: 56px; width: 100%; height: 106px;
    display: flex; align-items: center; justify-content: space-between; padding: 0 52px 0 56px;
  }
  .nav-title { font-size: 36px; font-weight: 500; letter-spacing: 0.3px; }

  .contact-photo {
    position: absolute; left: 113px; top: 222px; width: 548px; height: 706px;
    background:
      linear-gradient(180deg, rgba(0,0,0,0) 55%, var(--photo-shirt) 56%, var(--photo-shirt) 100%),
      radial-gradient(ellipse at 30% 15%, var(--photo-light) 0%, var(--photo-mid) 45%, var(--photo-dark) 100%);
  }

  .phone-field {
    position: absolute; left: 99px; top: 984px; width: 581px; height: 84px;
    border: 2px solid var(--field-border);
    display: flex; align-items: center; justify-content: center;
    font-size: 29px; font-weight: 700; color: var(--field-ink); letter-spacing: 0.5px;
  }

  .tool-bar {
    position: absolute; left: 0; bottom: 0; width: 777px; height: 94px;
    background: var(--bar);
    display: flex; align-items: center; justify-content: space-between; padding: 0 184px 0 186px;
  }
</style>
</head>
<body>
<main class="screen">
  <header class="top-bar">
    <div class="status-bar">
      <div class="status-left">
        <div class="signal"><span class="on"></span><span class="on"></span><span class="on"></span><span></span><span></span></div>
        <span class="carrier">NORVA</span>
        <svg width="24" height="18" viewBox="0 0 24 18" fill="none" stroke="#fff" stroke-width="2.4" stroke-linecap="round"><path d="M2 6a14 14 0 0 1 20 0"/><path d="M6 10a8 8 0 0 1 12 0"/><circle cx="12" cy="14.5" r="1.8" fill="#fff" stroke="none"/></svg>
      </div>
      <span class="clock">4:21 PM</span>
      <div class="status-right">
        <svg width="14" height="22" viewBox="0 0 14 22" fill="none" stroke="#fff" stroke-opacity=".7" stroke-width="1.6"><path d="M2 6l10 10-5 5V1l5 5L2 16"/></svg>
        <span>100%</span>
        <div class="battery"><div class="battery-fill"></div></div>
      </div>
    </div>
    <nav class="nav-bar">
      <svg class="back-icon" width="22" height="40" viewBox="0 0 22 40" fill="none" stroke="#fff" stroke-width="3" stroke-linecap="round" stroke-linejoin="round"><path d="M19 3L3 20l16 17"/></svg>
      <h1 class="nav-title">Add Contact</h1>
      <svg class="confirm-icon" width="46" height="46" viewBox="0 0 46 46" fill="none" stroke="#fff" stroke-width="2.6" stroke-linecap="round" stroke-linejoin="round"><path d="M36 24v17H4V9h24"/><path d="M12 22l9 9L43 4"/></svg>
    </nav>
  </header>

  <div class="contact-photo" role="img" aria-label="Portrait photo of the contact outdoors against blurred green foliage"></div>

  <div class="phone-field">517093462</div>

  <footer class="tool-bar">
    <svg class="delete-icon" width="44" height="56" viewBox="0 0 44 56" fill="none" stroke="#fff" stroke-width="2.6" stroke-linejoin="round"><path d="M2 10h40"/><path d="M16 10V3h12v7"/><path d="M6 10l2 43h28l2-43"/><path d="M15 18v28M22 18v28M29 18v28"/></svg>
    <svg class="gallery-icon" width="60" height="56" viewBox="0 0 60 56" fill="none" stroke="#fff" stroke-width="2.4" stroke-linejoin="round"><rect x="2" y="2" width="46" height="42"/><path d="M52 8v40H8"/><path d="M57 13v40H13"/><path d="M6 38l12-14 9 9 6-6 11 11"/><circle cx="14" cy="13" r="3.5"/></svg>
  </footer>
</main>
</body>
</html>
```